Update Pulp Parlor menu board to appear Fresh and modern

I need a menu board design that is not cluttered, easy to read, playful and the style of healthy and fresh for a juice bar. I will be editing the details of the items, so basically the design is all I need. I prefer the files to be in Microsoft Publisher as I am most familiar, but I have illustrator as well, but not as advanced on that. The size should be 36"x36". I will create 3 seperate boards from the one design.

Target Market(s)

health concious people, active lifestyle people

Font styles to use
Serif

Colors

Designer to choose colors to be used in the design.

Requirements
Must have
• Not cluttered
• Modern feel
Nice to have
• i like the style of the
• "cold pressed juice" part of my attached juice bottle label

```html
<!DOCTYPE html>
<html lang="en">
<head>
<meta charset="utf-8">
<title>Pulp Parlor Menu Board</title>
<link rel="stylesheet" href="https://fonts.googleapis.com/css2?family=Archivo:wght@800;900&family=Chango&family=Varela+Round&display=swap">
<style>
  :root {
    --orange: #f26922;
    --orange-soft: #f9a35a;
    --leaf: #cbe4b4;
    --panel: #fff2ea;
    --ink: #4a4a4a;
    --bar: #4d4d4d;
  }
  * { box-sizing: border-box; margin: 0; padding: 0; }
  html, body { width: 1200px; height: 1200px; overflow: hidden; }
  body { position: relative; background: var(--orange); font-family: "Varela Round", sans-serif; color: var(--ink); }
  .bar { position: absolute; left: 0; width: 1200px; background: var(--bar); }
  .bar--top { top: 0; height: 20px; }
  .bar--bottom { bottom: 0; height: 22px; }
  .backdrop {
    position: absolute; top: 20px; left: 0; width: 1200px; height: 1158px;
    background:
      radial-gradient(circle at 8% 95%, var(--orange-soft) 0 22%, transparent 23%),
      radial-gradient(circle at 75% 100%, var(--orange-soft) 0 18%, transparent 19%),
      radial-gradient(circle at 100% 45%, var(--orange-soft) 0 24%, transparent 25%),
      radial-gradient(circle at 78% 4%, var(--leaf) 0 7%, transparent 7.5%),
      radial-gradient(circle at 20% 4%, var(--leaf) 0 6%, transparent 6.5%),
      var(--orange);
  }
  .frame {
    position: absolute; top: 106px; width: 484px; height: 990px;
    border: 18px solid rgba(255,255,255,0.12); border-radius: 14px;
  }
  .frame--left { left: 76px; }
  .frame--right { left: 652px; }
  .panel {
    position: absolute; top: 124px; width: 448px; height: 955px;
    background: var(--panel); opacity: 0.96;
  }
  .panel--left { left: 94px; }
  .panel--right { left: 670px; }
  .section-title {
    position: absolute; font-family: "Archivo", sans-serif; font-weight: 800;
    font-size: 60px; letter-spacing: -0.045em; line-height: 1; color: var(--orange);
  }
  .section-sub {
    position: absolute; font-family: "Chango", sans-serif; font-size: 19px;
    line-height: 1; color: var(--ink); letter-spacing: 0.01em;
  }
  .rule { position: absolute; height: 10px; width: 399px; background: var(--orange); }
  .sizes {
    position: absolute; font-family: "Archivo", sans-serif; font-weight: 800;
    font-size: 14px; color: var(--ink);
  }
  .sizes span, .prices span { position: absolute; transform: translateX(-50%); white-space: nowrap; }
  .item { position: absolute; width: 400px; }
  .item-name {
    font-family: "Archivo", sans-serif; font-weight: 800; font-size: 27px;
    letter-spacing: -0.04em; line-height: 1; white-space: nowrap;
  }
  .prices {
    position: absolute; top: 0; left: 0; font-family: "Archivo", sans-serif;
    font-weight: 800; font-size: 27px; line-height: 1; letter-spacing: -0.03em;
  }
  .item-desc {
    margin: 5px 0 0 16px; font-size: 24px; line-height: 32px; letter-spacing: 0.035em; white-space: nowrap;
  }
  .shot {
    position: absolute; left: 125px; width: 390px; display: flex; justify-content: space-between;
    font-family: "Archivo", sans-serif; font-weight: 800; font-size: 27px;
    letter-spacing: -0.04em; line-height: 35px;
  }
</style>
</head>
<body>
  <div class="backdrop" role="img" aria-label="Pattern of large orange slices and green leaves across the background"></div>
  <div class="bar bar--top"></div>
  <div class="bar bar--bottom"></div>

  <div class="frame frame--left"></div>
  <div class="frame frame--right"></div>
  <div class="panel panel--left"></div>
  <div class="panel panel--right"></div>

  <!-- Fruit juices -->
  <h2 class="section-title" style="left:120px;top:156px;">FRUIT JUICES</h2>
  <p class="section-sub" style="left:125px;top:213px;">pick your squeeze!</p>
  <div class="rule" style="left:118px;top:248px;"></div>
  <div class="sizes" style="left:0;top:276px;"><span style="left:407px">SM</span><span style="left:456px">MD</span><span style="left:506px">LG</span></div>

  <div class="item" style="left:125px;top:314px;">
    <div class="item-name">Mango Madness</div>
    <div class="prices"><span style="left:278px">8</span><span style="left:330px">10</span><span style="left:381px">12</span></div>
    <p class="item-desc">Lorem ipsum dolor sit amet,<br>consectetuer adipiscing elit.</p>
  </div>
  <div class="item" style="left:125px;top:437px;">
    <div class="item-name">Go GREEN!</div>
    <div class="prices"><span style="left:278px">8</span><span style="left:330px">10</span><span style="left:381px">12</span></div>
    <p class="item-desc">Lorem ipsum dolor sit amet,<br>consectetuer adipiscing elit.</p>
  </div>
  <div class="item" style="left:125px;top:560px;">
    <div class="item-name">Pinapple</div>
    <div class="prices"><span style="left:278px">8</span><span style="left:330px">10</span><span style="left:381px">12</span></div>
    <p class="item-desc">Lorem ipsum dolor sit amet,<br>consectetuer adipiscing elit.</p>
  </div>
  <div class="item" style="left:125px;top:683px;">
    <div class="item-name">Tropic</div>
    <div class="prices"><span style="left:278px">8</span><span style="left:330px">10</span><span style="left:381px">12</span></div>
    <p class="item-desc">Lorem ipsum dolor sit amet,<br>consectetuer adipiscing elit.</p>
  </div>

  <!-- Shots -->
  <h2 class="section-title" style="left:120px;top:818px;">SHOTS</h2>
  <p class="section-sub" style="left:125px;top:875px;">6 oz. pour</p>
  <div class="rule" style="left:118px;top:910px;"></div>
  <div class="shot" style="top:940px;"><span>Wheatgrass</span><span>5.50</span></div>
  <div class="shot" style="top:975px;"><span>Kale</span><span>6.75</span></div>
  <div class="shot" style="top:1010px;"><span>Kombucha</span><span>4.75</span></div>

  <!-- Smoothies -->
  <h2 class="section-title" style="left:702px;top:156px;">SMOOTHIES</h2>
  <p class="section-sub" style="left:706px;top:213px;">pick your blend!</p>
  <div class="rule" style="left:697px;top:248px;"></div>
  <div class="sizes" style="left:0;top:276px;"><span style="left:979px">SM</span><span style="left:1029px">MD</span><span style="left:1079px">LG</span></div>

  <div class="item" style="left:697px;top:312px;">
    <div class="item-name">Mango Madness</div>
    <div class="prices"><span style="left:278px">8</span><span style="left:330px">10</span><span style="left:381px">12</span></div>
    <p class="item-desc">Lorem ipsum dolor sit amet,<br>consectetuer adipiscing elit.</p>
  </div>
  <div class="item" style="left:697px;top:435px;">
    <div class="item-name">Strawberry</div>
    <div class="prices"><span style="left:278px">8</span><span style="left:330px">10</span><span style="left:381px">12</span></div>
    <p class="item-desc">Lorem ipsum dolor sit amet,<br>consectetuer adipiscing elit.</p>
  </div>
  <div class="item" style="left:697px;top:558px;">
    <div class="item-name">Lemon</div>
    <div class="prices"><span style="left:278px">8</span><span style="left:330px">10</span><span style="left:381px">12</span></div>
    <p class="item-desc">Lorem ipsum dolor sit amet,<br>consectetuer adipiscing elit.</p>
  </div>
  <div class="item" style="left:697px;top:681px;">
    <div class="item-name">Banana Split</div>
    <div class="prices"><span style="left:278px">8</span><span style="left:330px">10</span><span style="left:381px">12</span></div>
    <p class="item-desc">Lorem ipsum dolor sit amet,<br>consectetuer adipiscing elit.</p>
  </div>
  <div class="item" style="left:697px;top:804px;">
    <div class="item-name">Strawberry</div>
    <div class="prices"><span style="left:278px">8</span><span style="left:330px">10</span><span style="left:381px">12</span></div>
    <p class="item-desc">Lorem ipsum dolor sit amet,<br>consectetuer adipiscing elit.</p>
  </div>
  <div class="item" style="left:697px;top:927px;">
    <div class="item-name">Lemon</div>
    <div class="prices"><span style="left:278px">8</span><span style="left:330px">10</span><span style="left:381px">12</span></div>
    <p class="item-desc">Lorem ipsum dolor sit amet,<br>consectetuer adipiscing elit.</p>
  </div>
</body>
</html>
```